CONTACT US Page and design for website

We need a contact us page for our website. We would like it to have a message area, a map, our information, etc.

Please see the text attachment for what we are looking for. We need to have something that is creative and interesting, modern and professional.

We believe that a contact US page should be very creative because everyone clicks that to contact us. We want it to be super professional, attention grabbing, pleasing to the eye.

PLEASE KEEP THE HEADER AND FOOTER THE SAME, ONLY THE ACTUAL CONTACT US PAGE NEEDS TO BE WORKED ON. THANKS!
We are excited to work with designers for this project.

Target Market(s)

Clients in technology business

Industry/Entity Type

Information Technology

Number of Pages Required

1 page

Font styles to use
Serif

Requirements
Must have
• CHECK THE TEXT ATTACHMENT PLEASE
• Must stay within our design colors and theme.
Nice to have
• see attachment
Should not have
• it should be special

```html
<!DOCTYPE html>
<html lang="en">
<head>
<meta charset="utf-8">
<title>Contact Us – Voltrix Tech</title>
<link href="https://fonts.googleapis.com/css2?family=Roboto:wght@300;400;500;700&display=swap" rel="stylesheet">
<style>
:root{
  --teal:#2fbfb3;
  --teal-dark:#239e94;
  --ink:#333;
  --muted:#666;
  --line:#e2e2e2;
  --map:#ebe8e3;
  --footer:#a6a6a6;
  --footer-dark:#8f8f8f;
  --white:#fff;
}
*{box-sizing:border-box;margin:0;padding:0}
html,body{width:889px;height:1200px;overflow:hidden}
body{font-family:"Roboto",Arial,sans-serif;color:var(--ink);background:var(--white);position:relative}
.abs{position:absolute}

/* header */
.site-header{position:absolute;left:0;top:0;width:889px;height:73px;border-bottom:1px solid var(--line)}
.brand{position:absolute;left:62px;top:22px;display:flex;align-items:center;gap:8px}
.brand-mark{width:24px;height:24px;background:var(--teal)}
.brand-name{font-size:24px;font-weight:400;letter-spacing:3px;color:var(--teal)}
.account-tab{position:absolute;left:691px;top:0;width:138px;height:25px;background:#8c8c8c;border-radius:0 0 16px 16px;display:flex;font-size:8px;color:#fff}
.account-tab span{flex:1;display:flex;align-items:center;justify-content:center}
.account-tab span:first-child{background:#a9a9a9;border-radius:0 0 0 16px}
.header-contact{position:absolute;top:32px;display:flex;align-items:center;gap:8px}
.round-icon{width:30px;height:30px;border:1px solid #ccc;border-radius:50%;display:flex;align-items:center;justify-content:center}
.live-chat{left:607px;font-size:10px;color:#444}
.header-phone{left:710px;font-size:14px;color:#222}

.main-nav{position:absolute;left:0;top:73px;width:889px;height:36px;display:flex;align-items:center}
.main-nav ul{list-style:none;display:flex;gap:19px;margin-left:61px;font-size:8px;color:#333}
.search{position:absolute;left:681px;top:81px;width:117px;height:23px;border:1px solid #ccc;border-radius:12px;font-size:8px;padding:7px 14px;color:#333}
.search svg{position:absolute;right:8px;top:5px}
.cart{position:absolute;left:805px;top:79px;width:27px;height:27px;border:1px solid #ccc;border-radius:50%;display:flex;align-items:center;justify-content:center}

.breadcrumb{position:absolute;left:0;top:109px;width:889px;height:25px;background:var(--teal);color:#fff;font-size:9px;padding:8px 0 0 119px}
.breadcrumb b{color:#1b3b39;font-weight:500}

.map-area{position:absolute;left:0;top:134px;width:889px;height:299px;background:linear-gradient(135deg,#efece6,#e6e4df 60%,#eceae5)}

/* contact */
.contact-title{position:absolute;left:62px;top:480px;font-size:22px;font-weight:400;color:#222}
.contact-lead{position:absolute;left:63px;top:523px;font-size:10px;color:#555}
.field{position:absolute;border:1px solid #ddd;font-size:10px;color:#999;padding:9px 12px}
.submit{position:absolute;left:62px;top:741px;width:156px;height:36px;background:var(--teal);border-bottom:3px solid var(--teal-dark);color:#fff;font-size:14px;font-weight:500;display:flex;align-items:center;justify-content:center}

.info-block{position:absolute;font-size:8.5px;color:#555;line-height:19px}
.info-block h3{font-size:10px;font-weight:500;color:#333;letter-spacing:.3px;line-height:14px;margin-bottom:5px;position:relative}
.info-block h3 svg{position:absolute;left:-17px;top:1px}
.info-block .group{margin-top:14px;color:#333;font-size:9px}
.info-row{display:flex;align-items:center;gap:8px}
.note{font-style:italic;color:var(--teal);font-size:7.5px;line-height:10px;margin-top:6px}

/* footer */
.site-footer{position:absolute;left:0;top:823px;width:889px;height:249px;background:var(--footer);color:#fff}
.footer-about{position:absolute;left:270px;top:32px;width:350px;text-align:center;font-size:10px;line-height:14.5px}
.footer-rule{position:absolute;left:270px;top:97px;width:400px;height:1px;background:rgba(255,255,255,.35)}
.footer-contact{position:absolute;top:130px;font-size:10px;display:flex;gap:8px;line-height:13px}
.footer-links{position:absolute;top:176px;font-size:11.5px}
.support-list{position:absolute;left:570px;top:192px;width:80px;text-align:center;font-size:7px;line-height:10.5px;list-style:none}
.footer-bottom{position:absolute;left:0;top:1072px;width:889px;height:128px;background:var(--footer-dark);color:#fff}
.social{position:absolute;top:16px;width:28px;height:28px;border:1px solid #ccc;border-radius:50%}
.bottom-rule{position:absolute;left:148px;top:58px;width:593px;height:1px;background:rgba(255,255,255,.4)}
.legal{position:absolute;left:408px;top:74px;font-size:9px;line-height:13.5px;display:flex;gap:7px}
.legal-mark{width:14px;height:14px;background:#fff;margin-top:3px}
.message-bar{position:absolute;left:710px;top:1180px;width:153px;height:20px;background:var(--teal);border:1px solid #fff;color:#fff;font-size:9px;font-weight:500;padding:4px 7px;display:flex;justify-content:space-between}
</style>
</head>
<body>

<header class="site-header">
  <div class="brand"><span class="brand-mark"></span><span class="brand-name">VOLTRIX TECH</span></div>
  <div class="account-tab"><span>SIGN UP</span><span>LOGIN</span></div>
  <div class="header-contact live-chat">
    <span class="round-icon"><svg width="12" height="10" viewBox="0 0 12 10"><path d="M1 1h7v5H4L2 8V6H1z" fill="#666"/><path d="M9 3h2v5h-1v2l-2-2H5V7h4z" fill="#888"/></svg></span>
    LIVE CHAT
  </div>
  <div class="header-contact header-phone">
    <span class="round-icon"><svg width="12" height="12" viewBox="0 0 12 12"><path d="M3 1l2 2-1 1.5c.8 1.6 1.9 2.7 3.5 3.5L9 7l2 2-1.5 2C5 10.5 1.5 7 1 2.5z" fill="#2fbfb3"/></svg></span>
    555-010-3013
  </div>
</header>

<nav class="main-nav">
  <ul><li>SERVERS</li><li>WORKSTATIONS</li><li>COMPONENTS</li><li>VIRTUAL REALITY</li><li>DRONES</li><li>ABOUT US</li><li>BLOG</li><li>RESOURCES</li><li>CONTACT US</li></ul>
</nav>
<div class="search">Search<svg width="12" height="12" viewBox="0 0 12 12"><circle cx="5" cy="5" r="3.5" stroke="#2fbfb3" stroke-width="1.6" fill="none"/><path d="M7.5 7.5l3 3" stroke="#2fbfb3" stroke-width="1.8"/></svg></div>
<div class="cart"><svg width="13" height="11" viewBox="0 0 13 11"><path d="M1 3h11l-1.5 7h-8z" fill="#2fbfb3"/><path d="M4 3l2-2M9 3L7 1" stroke="#2fbfb3"/></svg></div>

<div class="breadcrumb">HOME / <b>CONTACT US</b></div>

<div class="map-area" role="img" aria-label="Street map showing the office location"></div>

<main>
  <h1 class="contact-title">CONTACT US</h1>
  <p class="contact-lead">Contact us at the following for and general enquiries</p>

  <div class="field" style="left:62px;top:557px;width:212px;height:28px">Name *</div>
  <div class="field" style="left:284px;top:557px;width:213px;height:28px">Email *</div>
  <div class="field" style="left:62px;top:595px;width:435px;height:28px">Phone</div>
  <div class="field" style="left:62px;top:633px;width:435px;height:91px">Message *</div>
  <div class="submit">SUBMIT NOW!</div>

  <section class="info-block" style="left:542px;top:530px">
    <h3><svg width="8" height="10" viewBox="0 0 8 10"><path d="M4 0a4 4 0 0 1 4 4c0 3-4 6-4 6S0 7 0 4a4 4 0 0 1 4-4z" fill="#2fbfb3"/><circle cx="4" cy="4" r="1.5" fill="#fff"/></svg>OFFICE HEADQUARTERS</h3>
    <div>Voltrix Tech, LLC.</div>
    <div>4820 Marlow Ave. Cedar Vale,</div>
    <div>CA 90000</div>
  </section>

  <section class="info-block" style="left:542px;top:637px">
    <h3><svg width="9" height="9" viewBox="0 0 9 9"><circle cx="4.5" cy="4.5" r="3.7" stroke="#2fbfb3" stroke-width="1.2" fill="none"/><path d="M4.5 2.5v2h1.5" stroke="#2fbfb3" fill="none"/></svg>HOURS OF OPERATION</h3>
    <div>Monday: 8:00am- 5:00pm</div>
    <div>Tuesday: 8:00am- 5:00pm</div>
    <div>Wednesday: 8:00am- 5:00pm</div>
    <div>Thursday: 8:00am- 5:00pm</div>
    <div>Friday: 8:00am- 5:00pm</div>
    <p class="note">Our dedicated customer service<br>representatives are available 24/7 by phone.</p>
  </section>

  <section class="info-block" style="left:712px;top:530px">
    <h3><svg width="9" height="9" viewBox="0 0 9 9"><circle cx="4.5" cy="2.5" r="2.3" fill="#2fbfb3"/><path d="M0 9c0-3 2-4 4.5-4S9 6 9 9z" fill="#2fbfb3"/></svg>CONTACT INFO</h3>
    <div style="color:#333;font-size:9px">General Inquiries</div>
    <div class="info-row"><svg width="8" height="8" viewBox="0 0 12 12"><path d="M3 1l2 2-1 1.5c.8 1.6 1.9 2.7 3.5 3.5L9 7l2 2-1.5 2C5 10.5 1.5 7 1 2.5z" fill="#2fbfb3"/></svg>(555)010-3013</div>
    <div class="info-row"><svg width="9" height="7" viewBox="0 0 9 7"><rect width="9" height="7" fill="#2fbfb3"/><path d="M0 0l4.5 4L9 0" stroke="#fff" fill="none"/></svg>info@voltrixtech.com</div>
    <div class="group">Sales Inquiries</div>
    <div class="info-row"><svg width="8" height="8" viewBox="0 0 12 12"><path d="M3 1l2 2-1 1.5c.8 1.6 1.9 2.7 3.5 3.5L9 7l2 2-1.5 2C5 10.5 1.5 7 1 2.5z" fill="#2fbfb3"/></svg>(555)010-3013</div>
    <div class="info-row"><svg width="9" height="7" viewBox="0 0 9 7"><rect width="9" height="7" fill="#2fbfb3"/><path d="M0 0l4.5 4L9 0" stroke="#fff" fill="none"/></svg>sales@voltrixtech.com</div>
    <div class="group">Purchasing Inquiries</div>
    <div class="info-row"><svg width="8" height="8" viewBox="0 0 12 12"><path d="M3 1l2 2-1 1.5c.8 1.6 1.9 2.7 3.5 3.5L9 7l2 2-1.5 2C5 10.5 1.5 7 1 2.5z" fill="#2fbfb3"/></svg>(555)010-3014</div>
    <div class="info-row"><svg width="9" height="7" viewBox="0 0 9 7"><rect width="9" height="7" fill="#2fbfb3"/><path d="M0 0l4.5 4L9 0" stroke="#fff" fill="none"/></svg>purchasing@voltrixtech.com</div>
  </section>
</main>

<footer class="site-footer">
  <p class="footer-about">Based in Cedar Vale California, Voltrix Tech offers custom servers, storage, and workstations for local businesses in Los Angeles, Beverly Hills, Thousand Oaks, Ventura, Orange County, Santa Barbara, Oxnard, Irvine, Anaheim, and San Diego. Voltrix Tech also offers such products to clients throughout the United States and Worldwide.</p>
  <div class="footer-rule"></div>
  <div class="footer-contact" style="left:276px"><svg width="8" height="10" viewBox="0 0 8 10"><path d="M4 0a4 4 0 0 1 4 4c0 3-4 6-4 6S0 7 0 4a4 4 0 0 1 4-4z" fill="#fff"/></svg><span>4820 Marlow Ave.<br>Cedar Vale, CA 90000</span></div>
  <div class="footer-contact" style="left:407px"><svg width="9" height="9" viewBox="0 0 12 12"><path d="M3 1l2 2-1 1.5c.8 1.6 1.9 2.7 3.5 3.5L9 7l2 2-1.5 2C5 10.5 1.5 7 1 2.5z" fill="#fff"/></svg><span>555-010-3013</span></div>
  <div class="footer-contact" style="left:522px"><svg width="10" height="8" viewBox="0 0 9 7"><rect width="9" height="7" fill="#fff"/><path d="M0 0l4.5 4L9 0" stroke="#a6a6a6" fill="none"/></svg><span>sales@voltrixtech.com</span></div>
  <div class="footer-links" style="left:252px">Hardware</div>
  <div class="footer-links" style="left:349px">Drones</div>
  <div class="footer-links" style="left:419px">Retail</div>
  <div class="footer-links" style="left:497px">About</div>
  <div class="footer-links" style="left:561px">Customer Support</div>
  <ul class="support-list"><li>Terms and</li><li>Conditions</li><li>Warranty Information</li><li>Contact Us</li><li>Return Policy</li></ul>
</footer>

<div class="footer-bottom">
  <span class="social" style="left:367px"></span>
  <span class="social" style="left:405px"></span>
  <span class="social" style="left:443px"></span>
  <span class="social" style="left:481px"></span>
  <div class="bottom-rule"></div>
  <div class="legal"><span class="legal-mark"></span><span>Voltrix Tech, LLC.<br>Copyright © 2017</span></div>
</div>

<div class="message-bar"><span>Leave a message</span><svg width="10" height="10" viewBox="0 0 10 10"><path d="M1 7l4-4 4 4" stroke="#fff" stroke-width="1.6" fill="none"/></svg></div>

</body>
</html>
```